Diesel Fitting/Mechanical Company Needs a new Business Card

We would like a new business card that showcases our logo and business information.

Industry/Entity Type

Business

Contact Information for Business Card

314 Wendale Street
PO Box 7581 BRAYFIELD QLD 4917
Phone: 49312787 Fax: 49312688 Mobile: 0438915276 ABN: 63 519 087 342

Requirements
Must have
• The following email addresses:
• admin@tkservicing.com.au , sales@tkservicing.com.au , accounts@tkservicing.com.au , parts@tkservicing.com.au , office@tkservicing.com.au
• Also need to have the website: www.tkservicing.com.au

```html
<!DOCTYPE html>
<html lang="en">
<head>
<meta charset="utf-8">
<title>TK Servicing – Business Card Set</title>
<link rel="stylesheet" href="https://fonts.googleapis.com/css2?family=Questrial&display=swap">
<style>
  :root {
    --bg: #ece7e1;
    --card-dark: #2a2827;
    --card-light: #ffffff;
    --band: #231f20;
    --ink: #2b2b2b;
    --orange: #f07d1a;
    --white: #ffffff;
  }
  * { box-sizing: border-box; margin: 0; padding: 0; }
  html, body {
    width: 1200px; height: 1000px; overflow: hidden;
    background: var(--bg);
    font-family: "Questrial", "Century Gothic", sans-serif;
  }
  .sheet { position: relative; width: 1200px; height: 1000px; }

  .card {
    position: absolute;
    width: 28.75em; height: 16.5em;
    box-shadow: 0 0.2em 0.8em rgba(0,0,0,0.18);
    overflow: hidden;
  }
  .card--large { font-size: 16px; }
  .card--small { font-size: 12px; }
  .card--dark { background: var(--card-dark); }
  .card--light { background: var(--card-light); }

  /* Front */
  .brand {
    position: absolute; inset: 0;
    display: flex; align-items: center; justify-content: center; gap: 0.6em;
  }
  .brand__dot {
    width: 2.2em; height: 2.2em; border-radius: 50%;
    background: var(--orange);
  }
  .brand__name {
    font-size: 2.1em; color: var(--orange); letter-spacing: 0.01em;
  }
  .brand--white .brand__name { color: var(--white); }

  /* Back */
  .band {
    position: absolute; left: 0; right: 0; top: 1.9em; height: 3.1em;
    background: var(--band); color: var(--white);
    display: flex; flex-direction: column; align-items: center; justify-content: center;
    font-size: 1em; line-height: 1.3;
  }
  .band span { font-size: 0.82em; letter-spacing: 0.04em; }
  .contacts {
    position: absolute; left: 3.4em; right: 2.6em; top: 6.3em;
    display: flex; justify-content: space-between;
    color: var(--ink); font-size: 0.84em; line-height: 1.35;
  }
  .contacts ul { list-style: none; }
  .website {
    position: absolute; left: 0; right: 0; bottom: 1.5em;
    text-align: center; color: var(--orange); font-size: 0.8em;
  }
</style>
</head>
<body>
<main class="sheet">

  <!-- Row 1: main front and back -->
  <section class="card card--large card--dark" style="left:110px; top:100px;">
    <div class="brand"><span class="brand__dot"></span><span class="brand__name">TK Servicing</span></div>
  </section>

  <section class="card card--large card--light" style="left:630px; top:100px;">
    <div class="band"><span>314 Wendale Street PO Box 7581</span><span>BRAYFIELD QLD 4917</span></div>
    <div class="contacts">
      <ul>
        <li>admin@tkservicing.com.au</li>
        <li>sales@tkservicing.com.au</li>
        <li>accounts@tkservicing.com.au</li>
        <li>parts@tkservicing.com.au</li>
        <li>office@tkservicing.com.au</li>
      </ul>
      <ul>
        <li>Phone: 49312787</li>
        <li>Fax: 49312688</li>
        <li>Mobile: 0438915276</li>
        <li>ABN: 63 519 087 342</li>
      </ul>
    </div>
    <div class="website">www.tkservicing.com.au</div>
  </section>

  <!-- Row 2: front variants -->
  <section class="card card--small card--dark" style="left:45px; top:440px;">
    <div class="brand"><span class="brand__dot"></span><span class="brand__name">TK Servicing</span></div>
  </section>
  <section class="card card--small card--dark" style="left:427px; top:440px;">
    <div class="brand brand--white"><span class="brand__dot"></span><span class="brand__name">TK Servicing</span></div>
  </section>
  <section class="card card--small card--light" style="left:809px; top:440px;">
    <div class="brand"><span class="brand__dot"></span><span class="brand__name">TK Servicing</span></div>
  </section>

  <!-- Row 3: backs -->
  <section class="card card--small card--light" style="left:45px; top:700px;">
    <div class="band"><span>314 Wendale Street PO Box 7581</span><span>BRAYFIELD QLD 4917</span></div>
    <div class="contacts">
      <ul>
        <li>admin@tkservicing.com.au</li>
        <li>sales@tkservicing.com.au</li>
        <li>accounts@tkservicing.com.au</li>
        <li>parts@tkservicing.com.au</li>
        <li>office@tkservicing.com.au</li>
      </ul>
      <ul>
        <li>Phone: 49312787</li>
        <li>Fax: 49312688</li>
        <li>Mobile: 0438915276</li>
        <li>ABN: 63 519 087 342</li>
      </ul>
    </div>
    <div class="website">www.tkservicing.com.au</div>
  </section>
  <section class="card card--small card--light" style="left:427px; top:700px;">
    <div class="band"><span>314 Wendale Street PO Box 7581</span><span>BRAYFIELD QLD 4917</span></div>
    <div class="contacts">
      <ul>
        <li>admin@tkservicing.com.au</li>
        <li>sales@tkservicing.com.au</li>
        <li>accounts@tkservicing.com.au</li>
        <li>parts@tkservicing.com.au</li>
        <li>office@tkservicing.com.au</li>
      </ul>
      <ul>
        <li>Phone: 49312787</li>
        <li>Fax: 49312688</li>
        <li>Mobile: 0438915276</li>
        <li>ABN: 63 519 087 342</li>
      </ul>
    </div>
    <div class="website">www.tkservicing.com.au</div>
  </section>
  <section class="card card--small card--light" style="left:809px; top:700px;">
    <div class="band"><span>314 Wendale Street PO Box 7581</span><span>BRAYFIELD QLD 4917</span></div>
    <div class="contacts">
      <ul>
        <li>admin@tkservicing.com.au</li>
        <li>sales@tkservicing.com.au</li>
        <li>accounts@tkservicing.com.au</li>
        <li>parts@tkservicing.com.au</li>
        <li>office@tkservicing.com.au</li>
      </ul>
      <ul>
        <li>Phone: 49312787</li>
        <li>Fax: 49312688</li>
        <li>Mobile: 0438915276</li>
        <li>ABN: 63 519 087 342</li>
      </ul>
    </div>
    <div class="website">www.tkservicing.com.au</div>
  </section>

</main>
</body>
</html>
```